Tarnwick Nectar needs a great booklet

We need a booklet design for our Raw Honey business that is based in Dubai. Something clean and niche as our honey is special /very expensive. We have 12 types of honey and each type has its health benefits. As well we are very active on social media so will be good to be very creative and find a way through out this booklet to connect with the consumer. DO NOT inspire from the material i have send you (with the exception of wording)as this was done at the beginning of our business year so we would like something different.
I have attached the specs as we will be printing it in that format. We are looking to find a design source for future projects in various media formats.
Try to use a clean font and not funny ones (please try and find TARNWICK'S LOGO fonts)
For knowing more of who we are please have a look at our instagram account: tarnwicknectarae
THE FINAL DESIGN SHOULD LOOK LIKE A EDUCATIONAL BOOK FOR HONEY USERS BUT HAVE A PERSONAL FEEL. BE CREATIVE! HAVE FUN!
Updates

Please don't post anything that is similar to the options i got so far as it is a no for that kind. Added Wednesday, April 12, 2017

Industry/Entity Type

Business

Colors

Designer to choose colors to be used in the design.

Requirements
Must have
• a new look and please don't use the artwork/colors of the material i had send as that is to be used only for wording .
• File 1 - has the requirements for number of pages and size of booklet
Nice to have
• new and cool ideas
Should not have
• DO NOT inspire from the material i have send you (with the exception of wording)as this was done at the beginning of our business year so we would like something different.

```html
<!DOCTYPE html>
<html lang="en">
<head>
<meta charset="utf-8">
<title>Tarnwick Nectar — Booklet Cover Spread</title>
<link rel="stylesheet" href="https://fonts.googleapis.com/css2?family=Roboto+Condensed:wght@300;400;700&family=Lato:wght@400&display=swap">
<style>
  :root {
    --canvas: #ffffff;
    --page-white: #ffffff;
    --slate: #4a4d50;
    --slate-photo-a: #55585b;
    --slate-photo-b: #6c6f72;
    --gold: #d8c6a0;
    --gold-text: #cdb98d;
    --gold-strong: #d3bd8c;
    --ink: #44474a;
    --mark-dark: #1e1f21;
  }
  * { margin: 0; padding: 0; box-sizing: border-box; }
  html, body {
    width: 1200px; height: 589px; overflow: hidden;
    background: var(--canvas);
  }
  .spread {
    position: absolute;
    left: 92px; top: 119px;
    width: 1020px; height: 359px;
    background: var(--page-white);
    overflow: hidden;
  }
  .spread__art {
    position: absolute; inset: 0;
    width: 1020px; height: 359px;
  }

  /* Brand lockups: plain name with one simple shape beside it */
  .brand-lockup {
    position: absolute;
    display: flex;
    align-items: center;
    gap: 10px;
    transform: translate(-50%, -50%);
  }
  .brand-lockup__shape { flex: none; display: block; }
  .brand-lockup__name {
    font-family: "Roboto Condensed", Arial, sans-serif;
    font-weight: 700;
    text-transform: uppercase;
    line-height: 0.95;
    letter-spacing: 0.03em;
    white-space: nowrap;
  }
  .brand-lockup--back { left: 248px; top: 181px; }
  .brand-lockup--back .brand-lockup__shape {
    width: 30px; height: 30px; border-radius: 50%;
    border: 4px solid var(--page-white);
  }
  .brand-lockup--back .brand-lockup__name { font-size: 27px; color: var(--page-white); }

  .brand-lockup--front { left: 926px; top: 103px; }
  .brand-lockup--front .brand-lockup__shape {
    width: 30px; height: 30px;
    background: var(--mark-dark);
  }
  .brand-lockup--front .brand-lockup__name { font-size: 30px; color: var(--mark-dark); }

  .web-address {
    font-family: "Lato", Arial, sans-serif;
    font-size: 9.5px;
    letter-spacing: 0.42em;
    text-transform: none;
    white-space: nowrap;
  }
  .web-address--back {
    position: absolute;
    left: 248px; top: 234px;
    transform: translateX(-50%);
    color: var(--gold-text);
  }

  .tagline {
    position: absolute;
    right: 18px; top: 174px;
    text-align: right;
    font-family: "Roboto Condensed", Arial, sans-serif;
    white-space: nowrap;
  }
  .tagline__line { display: block; line-height: 1; text-transform: uppercase; }
  .tagline__brand { font-weight: 700; font-size: 25px; color: var(--slate); }
  .tagline__truly { font-weight: 300; font-size: 31px; color: var(--gold-text); margin-top: 3px; }
  .tagline__best { font-weight: 700; font-size: 22px; color: var(--gold-strong); margin-top: 4px; }
  .tagline__secret { font-weight: 400; font-size: 22px; color: var(--ink); margin-top: 4px; }
  .web-address--front { display: block; margin-top: 11px; color: var(--ink); margin-right: -4px; }
</style>
</head>
<body>
  <div class="spread">
    <svg class="spread__art" viewBox="0 0 1275 449" xmlns="http://www.w3.org/2000/svg">
      <defs>
        <linearGradient id="back-photo-tone" x1="0" y1="0" x2="1" y2="1">
          <stop offset="0" stop-color="var(--slate-photo-a)"/>
          <stop offset="0.5" stop-color="var(--slate-photo-b)"/>
          <stop offset="1" stop-color="var(--slate-photo-a)"/>
        </linearGradient>
        <linearGradient id="still-life-tone" x1="0" y1="0" x2="1" y2="1">
          <stop offset="0" stop-color="#d9d4cf"/>
          <stop offset="0.45" stop-color="#c96a55"/>
          <stop offset="0.7" stop-color="#9a5a2c"/>
          <stop offset="1" stop-color="#7a5238"/>
        </linearGradient>
      </defs>

      <rect class="back-page" x="0" y="0" width="636" height="449" fill="url(#back-photo-tone)" role="img" aria-label="Muted grey photograph of honeycomb filling the back cover"/>

      <polygon class="hex-frame hex-frame--dark" points="813,-10 813,31 977,126 1143,31 1143,-10" fill="none" stroke="var(--slate)" stroke-width="7"/>

      <polygon class="hex-frame hex-frame--lower" points="470,460 470,436 635,341 803,436 803,460" fill="var(--page-white)" stroke="var(--gold)" stroke-width="7"/>

      <polygon class="hex-frame hex-frame--feature" points="805,41 973,136 973,327 805,423 637,327 637,136" fill="var(--page-white)" stroke="var(--gold)" stroke-width="7"/>
      <polygon class="hex-photo" points="805,52 963,142 963,321 805,412 647,321 647,142" fill="url(#still-life-tone)" role="img" aria-label="Photograph of a jar of raw honey beside bowls of strawberries and figs on a wooden board"/>
    </svg>

    <div class="brand-lockup brand-lockup--back">
      <span class="brand-lockup__shape"></span>
      <span class="brand-lockup__name">Tarnwick<br>Nectar</span>
    </div>
    <span class="web-address web-address--back">tarnwicknectar.co</span>

    <div class="brand-lockup brand-lockup--front">
      <span class="brand-lockup__shape"></span>
      <span class="brand-lockup__name">Tarnwick<br>Nectar</span>
    </div>

    <div class="tagline">
      <span class="tagline__line tagline__brand">Tarnwick Nectar</span>
      <span class="tagline__line tagline__truly">Is Truly</span>
      <span class="tagline__line tagline__best">The World’s Best</span>
      <span class="tagline__line tagline__secret">Kept Secret</span>
      <span class="web-address web-address--front">tarnwicknectar.co</span>
    </div>
  </div>
</body>
</html>
```